Unique Beautiful Realtor business card

I need a unique business card that includes my logo, my firms logo, my picture and phone number. The colors should compliment my logo.

Target Market(s)

People who want to buy or sell a home in South Florida

Contact Information for Business Card

Use two sides and work with the TMQ Coastal Dwellings logo as a theme.
The Dorsett Ambrose should be small and discreet, it is a requirement to be there but should be small. My photo should be integrated artistically.

Font styles to use
Serif
Sans Serif

Colors

Designer to choose colors to be used in the design.

Requirements
Must have
• My logo, Dorsett Ambrose logo, my photo, my phone number, (555-203-8846) and my website address. (www.tmqcoastaldwellings.example)
• Also my name, Marla J. Quenby, PA, Realtor
• Also “The Garden Minded Realtor”

```html
<!DOCTYPE html>
<html lang="en">
<head>
<meta charset="utf-8">
<title>TMQ Coastal Dwellings – Business Card</title>
<link href="https://fonts.googleapis.com/css2?family=Roboto:ital,wght@0,400;0,500;0,700;1,500&display=swap" rel="stylesheet">
<style>
  :root {
    --page-bg: #e4e4e4;
    --card-white: #ffffff;
    --navy: #0b4a86;
    --sky: #0099d4;
    --text-grey: #555b61;
    --hair: #b89a6e;
    --jacket: #3b3f46;
  }
  * { margin: 0; padding: 0; box-sizing: border-box; }
  html, body { width: 1200px; height: 1200px; overflow: hidden; }
  body {
    background: var(--page-bg);
    font-family: 'Roboto', Arial, sans-serif;
    position: relative;
  }
  .card {
    position: absolute;
    left: 262px;
    width: 686px;
    height: 392px;
    overflow: hidden;
  }
  .card--front { top: 165px; background: var(--card-white); }
  .card--back { top: 653px; background: var(--sky); }

  /* Front */
  .brand-name {
    position: absolute;
    left: 52px; top: 60px;
    display: flex; align-items: center; gap: 12px;
    font-size: 28px; font-weight: 700; color: var(--navy);
    line-height: 1.1; width: 260px;
  }
  .brand-name .mark {
    flex: none; width: 20px; height: 20px; background: var(--navy);
  }
  .contact-list {
    position: absolute; left: 52px; top: 258px;
    list-style: none; font-size: 14.5px; color: var(--text-grey);
  }
  .contact-list li { display: flex; align-items: center; gap: 9px; height: 21.5px; white-space: nowrap; }
  .contact-list svg { width: 14px; height: 14px; flex: none; }
  .tagline {
    position: absolute; left: 53px; top: 340px;
    font-size: 15.5px; font-style: italic; font-weight: 500; color: var(--navy);
  }
  .accent-bar {
    position: absolute; left: 0; bottom: 0; width: 340px; height: 12px; background: var(--sky);
  }
  .portrait {
    position: absolute; left: 0; top: 0; width: 686px; height: 392px;
  }
  .name-panel {
    position: absolute; left: 0; top: 0; width: 686px; height: 392px;
  }
  .name-block {
    position: absolute; right: 42px; top: 332px; text-align: right; color: #fff;
  }
  .name-block .person { font-size: 26px; font-weight: 500; line-height: 1.1; }
  .name-block .role { font-size: 17px; font-weight: 500; }

  /* Back */
  .firm-name {
    position: absolute; left: 41px; top: 46px;
    display: flex; align-items: center; gap: 7px;
    font-size: 13px; font-weight: 500; color: #fff; letter-spacing: 0.2px;
  }
  .firm-name .mark { width: 10px; height: 10px; background: #fff; }
  .back-brand {
    position: absolute; left: 0; right: 0; top: 145px; text-align: center;
    font-size: 44px; font-weight: 700; color: var(--navy);
  }
  .back-url {
    position: absolute; left: 0; right: 0; top: 338px; text-align: center;
    font-size: 16px; color: #fff; letter-spacing: 5.4px;
  }
</style>
</head>
<body>
  <section class="card card--front">
    <div class="brand-name"><span class="mark"></span><span>TMQ Coastal Dwellings</span></div>

    <ul class="contact-list">
      <li>
        <svg viewBox="0 0 16 16"><path fill="#0b4a86" d="M3.5 1l2.5 3-1.5 1.8c.8 1.9 2.4 3.5 4.2 4.3L10.5 8.6 13.5 11l-1.3 2.8C6.5 13.5 2.5 9.5 1 3.5z"/></svg>
        <span>(555-203-8846)</span>
      </li>
      <li>
        <svg viewBox="0 0 16 16"><rect x="1" y="3.5" width="14" height="9" fill="#0b4a86"/><path d="M1.5 4l6.5 5 6.5-5" stroke="#fff" stroke-width="1.3" fill="none"/></svg>
        <span>info@tmqcoastaldwellings.example</span>
      </li>
      <li>
        <svg viewBox="0 0 16 16"><circle cx="8" cy="8" r="7" fill="#0b4a86"/><path d="M1 8h14M8 1c-3 3-3 11 0 14M8 1c3 3 3 11 0 14" stroke="#fff" stroke-width="1" fill="none"/></svg>
        <span>www.tmqcoastaldwellings.example</span>
      </li>
    </ul>

    <p class="tagline">The Garden Minded Realtor</p>
    <div class="accent-bar"></div>

    <svg class="portrait" viewBox="0 0 686 392" role="img" aria-label="Cut-out portrait photo of the realtor with long blond hair in a grey blazer">
      <defs>
        <linearGradient id="jacketTone" x1="0" y1="0" x2="0" y2="1">
          <stop offset="0" stop-color="#55595f"/>
          <stop offset="1" stop-color="#33363b"/>
        </linearGradient>
        <radialGradient id="hairTone" cx="0.5" cy="0.4" r="0.6">
          <stop offset="0" stop-color="#d8c2a0"/>
          <stop offset="1" stop-color="#a68758"/>
        </radialGradient>
      </defs>
      <path d="M415 192 L686 190 L686 392 L345 392 L360 320 L385 250 Z" fill="url(#jacketTone)"/>
      <ellipse cx="543" cy="135" rx="88" ry="118" fill="url(#hairTone)"/>
    </svg>

    <svg class="name-panel" viewBox="0 0 686 392" aria-hidden="true">
      <polygon points="385,322 686,322 686,392 329,392" fill="#0b4a86"/>
      <polygon points="333,380 340,380 330,392 323,392" fill="#0099d4"/>
    </svg>
    <div class="name-block">
      <div class="person">Marla J. Quenby, PA</div>
      <div class="role">Realtor</div>
    </div>
  </section>

  <section class="card card--back">
    <div class="firm-name"><span class="mark"></span><span>Harbor Point · Dorsett Ambrose</span></div>
    <div class="back-brand">TMQ Coastal Dwellings</div>
    <div class="back-url">www.tmqcoastaldwellings.example</div>
  </section>
</body>
</html>
```